Kentucky residential recovery center needs a flyer design

We need a flyer design for a 16 bed male residential/inpatient recovery center based in Larkford, Ohio. The facility provides short term (average 30 day) treatment to those struggling with substace abuse and addiction. The design should communicate trust, assurance, safety.
Our wesite provides more information https://morvalcare.org/treatment-services/residential-treatment/

Target Market(s)

Men (typically 30-50) struggling with substance addiction

```html
<!DOCTYPE html>
<html lang="en">
<head>
<meta charset="utf-8">
<title>Morval Care – Residential Recovery Center Flyer</title>
<link href="https://fonts.googleapis.com/css2?family=Open+Sans:wght@400;600;700;800&family=Barlow+Condensed:wght@500&display=swap" rel="stylesheet">
<style>
  :root {
    --stage: #a7b7d4;
    --paper: #bdd4e4;
    --paper-light: #cfe0ec;
    --navy: #14146b;
    --green: #1a9a2c;
    --green-text: #0f8a22;
    --box: #e6eaee;
    --divider: #9aa6a6;
    --white: #ffffff;
    --photo-top: #8a7c69;
    --photo-bottom: #3f372e;
  }
  * { box-sizing: border-box; margin: 0; padding: 0; }
  html, body { width: 1200px; height: 900px; overflow: hidden; }
  body {
    background: var(--stage);
    font-family: "Open Sans", Arial, sans-serif;
    position: relative;
  }
  .flyer {
    position: absolute;
    left: 300px; top: 39px;
    width: 600px; height: 822px;
    background: linear-gradient(160deg, var(--paper-light), var(--paper) 60%);
    overflow: hidden;
    box-shadow: 0 14px 30px rgba(40,60,100,.25);
  }
  .hero { position: absolute; left: 0; top: 0; width: 600px; height: 330px; }
  .headline {
    position: absolute; left: 110px; top: 134px; width: 380px;
    text-align: center; color: var(--white);
    text-shadow: 0 1px 3px rgba(0,0,0,.5);
  }
  .headline .beds { font-size: 40px; font-weight: 600; line-height: 1; letter-spacing: .5px; }
  .headline .kind { font-size: 20px; font-weight: 600; line-height: 1.05; }
  .brand-seal {
    position: absolute; left: 228px; top: 236px; width: 144px; height: 144px;
    border-radius: 50%; background: var(--white);
    box-shadow: 0 2px 6px rgba(0,0,0,.3);
    display: flex; align-items: center; justify-content: center;
  }
  .brand-name { color: var(--navy); font-weight: 700; font-size: 20px; }
  .intro {
    position: absolute; left: 40px; top: 390px; width: 520px;
    text-align: center; color: var(--navy); font-size: 18px; line-height: 23px;
  }
  .intro .highlight { color: var(--white); font-weight: 700; }
  .issues {
    position: absolute; left: 24px; top: 469px; width: 548px; height: 124px;
    background: var(--box); border-radius: 12px;
    box-shadow: 0 3px 6px rgba(0,0,0,.2);
  }
  .issues-title { position: absolute; left: 18px; top: 26px; color: var(--navy); }
  .issues-title .eyebrow { color: var(--green-text); font-size: 13px; font-weight: 700; }
  .issues-title .main { font-size: 31px; font-weight: 800; line-height: 1.05; }
  .issues-title .sub { font-size: 18px; line-height: 1.1; }
  .issues-divider { position: absolute; left: 270px; top: 12px; width: 1px; height: 100px; background: var(--divider); }
  .issues-arrow { position: absolute; left: 268px; top: 51px; }
  .issues-list { position: absolute; left: 300px; top: 10px; list-style: none; }
  .issues-list li {
    display: flex; align-items: center; gap: 10px;
    color: var(--green-text); font-weight: 700; font-size: 17px; line-height: 25.5px;
  }
  .issues-list svg { width: 18px; height: 18px; }
  .services { position: absolute; left: 30px; top: 608px; }
  .services h2 { color: var(--green-text); font-size: 20px; font-weight: 800; margin-bottom: 4px; }
  .services ul { list-style: none; font-family: "Barlow Condensed", "Arial Narrow", sans-serif;
    color: var(--navy); font-size: 15px; font-weight: 500; line-height: 22.5px; }
  .room-photo { position: absolute; border-radius: 8px; border: 2px solid var(--white); }
  .room-photo.lounge { left: 364px; top: 614px; width: 98px; height: 94px;
    background: linear-gradient(160deg, #6d6259, #3a302a); }
  .room-photo.bedroom { left: 467px; top: 650px; width: 98px; height: 94px;
    background: linear-gradient(160deg, #b9b4aa, #6e5a45); }
  .contact-label { position: absolute; left: 0; top: 761px; width: 600px; text-align: center;
    color: var(--navy); font-size: 14.5px; font-weight: 800; }
  .contact-band { position: absolute; left: 0; top: 783px; width: 600px; height: 39px;
    background: var(--green); color: var(--white); font-size: 14.5px;
    display: flex; align-items: center; justify-content: center; gap: 18px; }
  .contact-band span { display: flex; align-items: center; gap: 5px; }
</style>
</head>
<body>
<main class="flyer">
  <svg class="hero" viewBox="0 0 600 330" role="img" aria-label="Photo of two smiling men holding recovery certificates in a dormitory room with bunk beds">
    <defs>
      <linearGradient id="hero-tone" x1="0" y1="0" x2="0" y2="1">
        <stop offset="0" stop-color="var(--photo-top)"/>
        <stop offset="1" stop-color="var(--photo-bottom)"/>
      </linearGradient>
    </defs>
    <path d="M0 0 H600 V222 Q300 382 0 200 Z" fill="url(#hero-tone)"/>
    <path d="M0 204 Q300 386 600 226" fill="none" stroke="var(--green)" stroke-width="8"/>
    <path d="M0 212 Q300 394 600 234" fill="none" stroke="var(--navy)" stroke-width="8"/>
  </svg>
  <div class="headline">
    <div class="beds">16 BEDMALE</div>
    <div class="kind">RESIDENTIAL/INPATIENT<br>RECOVERY CENTER</div>
  </div>
  <div class="brand-seal"><span class="brand-name">Morval Care</span></div>

  <p class="intro">Based in Larkford, Ohio. The facility provides<br>short term <span class="highlight">(average 30 day)</span> treatment to those<br>struggling with substace abuse and addiction.</p>

  <section class="issues">
    <div class="issues-title">
      <div class="eyebrow">Problems we can help with</div>
      <div class="main">WHAT ISSUES</div>
      <div class="sub">CAN BE TREATED?</div>
    </div>
    <div class="issues-divider"></div>
    <svg class="issues-arrow" width="16" height="22" viewBox="0 0 16 22"><path d="M0 0 L16 11 L0 22 Z" fill="var(--green)"/></svg>
    <ul class="issues-list">
      <li><svg viewBox="0 0 18 18"><rect x="6" y="1" width="6" height="4" fill="none" stroke="var(--navy)"/><rect x="4" y="5" width="10" height="12" rx="2" fill="none" stroke="var(--navy)"/></svg>Alcoholism</li>
      <li><svg viewBox="0 0 18 18"><path d="M2 16 L14 4 M11 1 L17 7 M4 11 L7 14" stroke="var(--navy)" stroke-width="1.5" fill="none"/></svg>Drug addiction</li>
      <li><svg viewBox="0 0 18 18"><circle cx="6" cy="6" r="4" fill="none" stroke="var(--navy)"/><rect x="8" y="9" width="9" height="5" rx="2.5" fill="none" stroke="var(--navy)"/></svg>Medication addiction</li>
      <li><svg viewBox="0 0 18 18"><path d="M4 16 V11 Q1 8 3 4 Q7 0 12 2 Q16 5 14 10 V16" fill="none" stroke="var(--navy)"/><circle cx="9" cy="7" r="2" fill="none" stroke="var(--navy)"/></svg>Behavioral health</li>
    </ul>
  </section>

  <section class="services">
    <h2>SERVICES OFFERED BY US:</h2>
    <ul>
      <li>• OUTPATIENT &nbsp;• INTENSIVE OUTPATIENT• RESIDENTIAL</li>
      <li>• TARGETED CASE MANAGEMENT • PEER SUPPORT</li>
      <li>• INDIVIDUAL AND GROUP THERAPY</li>
      <li>• MEDICATED ASSISTED TREATMENT (‘MAT’)</li>
      <li>• PHYSICIAN APPOINTMENTS • TELEMEDICINE</li>
    </ul>
  </section>
  <div class="room-photo lounge" role="img" aria-label="Photo of the facility lounge with sofas and a television"></div>
  <div class="room-photo bedroom" role="img" aria-label="Photo of a resident bedroom with bunk beds"></div>

  <div class="contact-label">CONTACT US TODAY</div>
  <div class="contact-band">
    <span><svg width="14" height="14" viewBox="0 0 14 14"><circle cx="7" cy="7" r="6" fill="none" stroke="#fff"/><path d="M4.5 4 L6 4 L6.5 5.5 L5.7 6.2 Q6.5 7.8 7.8 8.3 L8.5 7.5 L10 8 L10 9.5 Q6 10 4.5 4 Z" fill="#fff"/></svg>859-555-0142</span>
    <span><svg width="14" height="11" viewBox="0 0 14 11"><rect x=".5" y=".5" width="13" height="10" fill="none" stroke="#fff"/><path d="M.5 .5 L7 6 L13.5 .5" fill="none" stroke="#fff"/></svg>admissions@morvalcare.org</span>
  </div>
</main>
</body>
</html>
```